Building/Renovation Company needs Website

I need a website designed for a renovation/building company based in Hampshire. We specialise in kitchens, bathrooms, carpentry, plastering, brickwork, ground/garden works and decorating, and all our work is fully insured and carried out to a high standard.

With the photos, display them in a before/after format.

Coding

Coded - Design and coding required

Number of Pages Required

1 page

```html
<!DOCTYPE html>
<html lang="en">
<head>
<meta charset="utf-8">
<title>Hartwell Developments – Property Renovation &amp; Building Services</title>
<link href="https://fonts.googleapis.com/css2?family=Oswald:wght@300;400;500&family=Poppins:wght@400;500;600&display=swap" rel="stylesheet">
<style>
:root{
  --blue:#2a3590;
  --blue-dark:#1f2877;
  --lime:#d4df2a;
  --ink:#111111;
  --body:#3a3a3a;
  --white:#ffffff;
  --card-line:#c9cde8;
  --head:'Oswald',sans-serif;
  --text:'Poppins',sans-serif;
}
*{margin:0;padding:0;box-sizing:border-box}
html,body{width:1200px;height:3570px;overflow:hidden}
body{position:relative;background:var(--white);font-family:var(--text);color:var(--ink)}
.abs{position:absolute}
.bg-shapes{position:absolute;left:0;top:0;width:1200px;height:3570px}
.btn{position:absolute;display:flex;align-items:center;justify-content:center;font-family:var(--text);font-weight:600;font-size:12px;text-decoration:none}
.btn-lime{background:var(--lime);color:var(--blue)}
.btn-blue{background:var(--blue);color:var(--white)}
.btn-outline{border:2px solid var(--lime);color:var(--blue);background:var(--white)}
.ph{position:absolute}

/* top bar */
.topbar-text{position:absolute;top:5px;font-size:10px;color:var(--white);display:flex;align-items:center;gap:5px;font-weight:500}
.brand{position:absolute;display:flex;align-items:center;gap:10px;font-family:var(--text);font-weight:500}
.brand .mark{background:var(--lime)}
.nav{position:absolute;top:47px;left:630px;display:flex;gap:21px;font-size:12px}
.nav a{color:var(--ink);text-decoration:none}
.nav a.active{color:var(--lime);border-bottom:1px solid var(--lime);padding-bottom:2px}

.hero-title{position:absolute;left:89px;top:200px;font-family:var(--head);font-weight:400;font-size:41px;line-height:52px;color:var(--ink)}
.hero-title em{font-style:normal;color:var(--lime)}

.services-kicker{position:absolute;left:0;width:1200px;top:884px;text-align:center;font-family:var(--head);font-weight:300;font-size:28px;color:var(--white)}
.services-title{position:absolute;left:0;width:1200px;top:918px;text-align:center;font-family:var(--head);font-weight:400;font-size:53px;color:var(--lime)}
.slide-arrow{position:absolute;width:25px;height:25px;background:var(--blue-dark);color:var(--white);font-size:11px;display:flex;align-items:center;justify-content:center}
.service-card{position:absolute;top:1008px;width:249px;height:323px;background:var(--white);border:2px solid var(--card-line);box-shadow:0 12px 30px rgba(40,50,120,.15)}
.service-card .photo{height:267px}
.service-card h3{font-family:var(--head);font-weight:400;font-size:19px;padding:14px 0 0 30px}

.about-kicker{position:absolute;left:648px;top:1536px;font-family:var(--head);font-size:20px;font-weight:400}
.about-title{position:absolute;left:648px;top:1558px;font-family:var(--head);font-size:46px;font-weight:400}
.about-copy{position:absolute;left:648px;width:380px;font-size:12.4px;line-height:19px;color:var(--body)}

.section-title{position:absolute;left:0;width:1200px;text-align:center;font-family:var(--head);font-weight:400;font-size:44px}
.why-card{position:absolute;top:2076px;width:185px;height:185px;background:var(--white);box-shadow:0 10px 28px rgba(40,50,120,.10);display:flex;flex-direction:column;align-items:center;justify-content:flex-start;padding-top:42px;text-align:center}
.why-card.featured{border:1.5px solid var(--card-line)}
.why-card p{font-family:var(--head);font-size:15px;line-height:19px;color:var(--blue);margin-top:14px}

.gallery-arrow{position:absolute;width:44px;height:44px;display:flex;align-items:center;justify-content:center}

.cta-title{position:absolute;left:91px;top:3152px;font-family:var(--head);font-weight:400;font-size:36px;color:var(--white)}
.cta-title em{font-style:normal;color:var(--lime)}
.cta-sub{position:absolute;left:91px;top:3208px;font-size:12.5px;color:var(--white)}
.rule{position:absolute;left:91px;width:1019px;height:1px;background:rgba(255,255,255,.22)}
.contact-item{position:absolute;top:3384px;display:flex;gap:14px}
.contact-item .label{font-family:var(--head);font-size:14px;color:var(--lime)}
.contact-item .value{font-family:var(--head);font-size:21px;color:var(--white);margin-top:2px}
.copyright{position:absolute;left:0;width:1200px;top:3535px;text-align:center;font-size:12.5px;color:var(--white)}
.to-top{position:absolute;left:1136px;top:3497px;width:39px;height:39px;background:var(--lime);display:flex;align-items:center;justify-content:center}
</style>
</head>
<body>

<!-- background shapes -->
<svg class="bg-shapes" viewBox="0 0 1200 3570" aria-hidden="true">
  <polygon points="679,0 1200,0 1200,25 710,25" fill="var(--blue)"/>
  <polygon points="0,560 1200,398 1200,690 0,860" fill="var(--lime)"/>
  <polygon points="0,860 1200,680 1200,1278 0,1146" fill="var(--blue)"/>
  <polygon points="0,2991 1200,3126 1200,3570 0,3570" fill="var(--blue)"/>
  <rect x="1197" y="2835" width="3" height="290" fill="var(--blue-dark)"/>
</svg>

<!-- header -->
<div class="topbar-text" style="left:748px">
  <svg width="9" height="9" viewBox="0 0 24 24"><path d="M6.6 10.8a15 15 0 0 0 6.6 6.6l2.2-2.2a1 1 0 0 1 1-.25 11.4 11.4 0 0 0 3.6.57 1 1 0 0 1 1 1V20a1 1 0 0 1-1 1A17 17 0 0 1 3 4a1 1 0 0 1 1-1h3.5a1 1 0 0 1 1 1c0 1.25.2 2.45.57 3.6a1 1 0 0 1-.25 1z" fill="var(--lime)"/></svg>
  Call Us: 07700 900418
</div>
<div class="topbar-text" style="left:896px">
  <svg width="10" height="8" viewBox="0 0 24 18"><rect width="24" height="18" rx="2" fill="var(--lime)"/><path d="M1 2l11 8 11-8" stroke="var(--blue)" stroke-width="2" fill="none"/></svg>
  Email Us: hello@hartwellbuild.co.uk
</div>

<div class="brand" style="left:88px;top:30px">
  <span class="mark" style="width:26px;height:26px"></span>
  <span style="font-size:19px;color:var(--blue)">Hartwell Developments</span>
</div>

<nav class="nav">
  <a class="active" href="#">Home</a><a href="#">Services</a><a href="#">Portfolio</a><a href="#">About</a><a href="#">Contact</a>
</nav>
<a class="btn btn-lime" href="#" style="left:949px;top:39px;width:160px;height:39px">Get Your Free Quote</a>

<!-- hero -->
<h1 class="hero-title">Delivering <em>High Quality</em><br>workmaship across Hamshire<br>and surrounding countries.</h1>
<a class="btn btn-blue" href="#" style="left:90px;top:367px;width:150px;height:41px">Get a Free Quote</a>
<a class="btn btn-outline" href="#" style="left:249px;top:367px;width:135px;height:41px">View Our Work</a>

<div class="ph" role="img" aria-label="Illustration of a house under construction with scaffolding and builders at work" style="left:552px;top:132px;width:620px;height:554px;background:radial-gradient(ellipse at 50% 55%,#b9a88e 0%,#d6cdbd 45%,rgba(255,255,255,0) 72%)"></div>
<div class="ph" role="img" aria-label="Photo of a worn builder's trowel" style="left:0;top:548px;width:395px;height:180px;background:radial-gradient(ellipse at 55% 55%,#8a5a3a 0%,#a88363 40%,rgba(212,223,42,0) 72%)"></div>

<!-- services -->
<p class="services-kicker">Property Renovation &amp;</p>
<h2 class="services-title">Building Services</h2>
<div class="slide-arrow" style="left:1050px;top:949px">&#8249;</div>
<div class="slide-arrow" style="left:1084px;top:949px">&#8250;</div>

<div class="service-card" style="left:93px">
  <div class="photo" role="img" aria-label="Photo of a bricklayer in hi-vis laying bricks" style="background:linear-gradient(180deg,#cfd8df 0%,#c9c66a 45%,#a85a3e 100%)"></div>
  <h3>Brickwork</h3>
</div>
<div class="service-card" style="left:349px">
  <div class="photo" role="img" aria-label="Photo of a carpentry workshop with a trainee holding timber" style="background:linear-gradient(180deg,#a98a62 0%,#c2b55a 50%,#6d5a42 100%)"></div>
  <h3>Carpentry</h3>
</div>
<div class="service-card" style="left:606px">
  <div class="photo" role="img" aria-label="Photo of a plumber fitting bathroom pipework" style="background:linear-gradient(180deg,#ecebe6 0%,#d7d3cc 55%,#b54a45 100%)"></div>
  <h3>Bathroom Fittings</h3>
</div>
<div class="service-card" style="left:861px">
  <div class="photo" role="img" aria-label="Photo of a tradesman with tool belt in a kitchen" style="background:linear-gradient(180deg,#e7eaee 0%,#7f95b8 55%,#4d5f80 100%)"></div>
  <h3>Kitchen Fittings</h3>
</div>
<a class="btn btn-lime" href="#" style="left:510px;top:1376px;width:180px;height:41px">Veiw All Services</a>

<!-- about -->
<svg class="abs" style="left:151px;top:1490px" width="402" height="410" aria-hidden="true">
  <polyline points="76,90 76,56 202,56" fill="none" stroke="var(--lime)" stroke-width="2"/>
  <polyline points="348,200 348,270" fill="none" stroke="var(--lime)" stroke-width="2"/>
  <polyline points="270,313 291,313" fill="none" stroke="var(--lime)" stroke-width="2"/>
</svg>
<div class="ph" role="img" aria-label="Photo of a worker in a hard hat inspecting a trench" style="left:353px;top:1490px;width:188px;height:201px;background:linear-gradient(160deg,#c9a56a 0%,#b38c52 50%,#d7d35a 100%)"></div>
<div class="ph" role="img" aria-label="Photo of a surveyor with a theodolite near a crane" style="left:151px;top:1580px;width:270px;height:319px;background:linear-gradient(180deg,#7aa2d4 0%,#9fb9d8 50%,#8b8f7a 100%)"></div>
<div class="ph" role="img" aria-label="Photo of groundworks with a worker laying pipe" style="left:442px;top:1760px;width:110px;height:117px;background:linear-gradient(180deg,#5c6a4e 0%,#8f9a63 100%)"></div>

<p class="about-kicker">About</p>
<h2 class="about-title">Hartwell Development</h2>
<p class="about-copy" style="top:1620px">At Hartwell Developments, we specialise in complete property renovation and building services tailored to your needs. Whether it's small improvements or full-scale refurbishments, our experienced team delivers exceptional results with high-quality finishes you can rely on.</p>
<p class="about-copy" style="top:1731px">We take pride in our workmanship, attention to detail, and commitment to customer satisfaction. Every project is handled with professionalism, care, and efficiency.</p>
<a class="btn btn-lime" href="#" style="left:648px;top:1808px;width:126px;height:40px">Read More</a>

<!-- why choose -->
<h2 class="section-title" style="top:1985px">Why Choose Hartwell Developments?</h2>

<div class="why-card" style="left:114px">
  <svg width="52" height="56" viewBox="0 0 52 56"><path d="M26 3 L47 11 V28 C47 41 37 50 26 53 C15 50 5 41 5 28 V11 Z" fill="none" stroke="var(--lime)" stroke-width="2.5"/><path d="M26 10 L41 16 V28 C41 38 34 44 26 47 C18 44 11 38 11 28 V16 Z" fill="none" stroke="var(--lime)" stroke-width="1.5"/><path d="M18 28 l6 6 11-12" fill="none" stroke="var(--lime)" stroke-width="2.5"/></svg>
  <p>Fully Insured Work</p>
</div>
<div class="why-card featured" style="left:310px">
  <svg width="64" height="56" viewBox="0 0 64 56"><path d="M4 22 L16 10 L28 16 L36 12 L48 10 L60 22 L48 40 L40 48 L32 44 L24 48 L14 38 Z" fill="none" stroke="var(--blue)" stroke-width="2.5" stroke-linejoin="round"/><path d="M28 16 L22 26 L30 28 L38 20 L48 32" fill="none" stroke="var(--blue)" stroke-width="2.5" stroke-linejoin="round"/></svg>
  <p>Reliable &amp;<br>Professional Team</p>
</div>
<div class="why-card" style="left:507px">
  <svg width="56" height="56" viewBox="0 0 56 56"><circle cx="28" cy="28" r="24" fill="none" stroke="var(--lime)" stroke-width="2.5" stroke-dasharray="9 3"/><circle cx="28" cy="28" r="15" fill="none" stroke="var(--lime)" stroke-width="2"/><path d="M21 28 l5 5 9-10" fill="none" stroke="var(--lime)" stroke-width="2.5"/></svg>
  <p>High-Quality Finishes</p>
</div>
<div class="why-card" style="left:704px">
  <svg width="56" height="56" viewBox="0 0 56 56"><path d="M28 2 l2 5 5 0-4 3 2 5-5-3-5 3 2-5-4-3 5 0z" fill="var(--lime)"/><path d="M28 20 l8 9 h-5 v24 h-6 V29 h-5z M12 32 l7 8 h-4 v13 h-6 V40 h-4z M44 32 l7 8 h-4 v13 h-6 V40 h-4z" fill="none" stroke="var(--lime)" stroke-width="2" stroke-linejoin="round"/></svg>
  <p>Competitive Pricing</p>
</div>
<div class="why-card" style="left:902px">
  <svg width="56" height="56" viewBox="0 0 24 24"><path d="M6.6 10.8a15 15 0 0 0 6.6 6.6l2.2-2.2a1 1 0 0 1 1-.25 11.4 11.4 0 0 0 3.6.57 1 1 0 0 1 1 1V20a1 1 0 0 1-1 1A17 17 0 0 1 3 4a1 1 0 0 1 1-1h3.5a1 1 0 0 1 1 1c0 1.25.2 2.45.57 3.6a1 1 0 0 1-.25 1z" fill="none" stroke="var(--lime)" stroke-width="1.2"/></svg>
  <p>Free, No<br>Obligation Quotes</p>
</div>

<!-- projects -->
<h2 class="section-title" style="top:2358px">Our Signature Projects</h2>
<div class="ph" role="img" aria-label="Before photo: rooftop terrace with new timber decking and garden view" style="left:222px;top:2445px;width:402px;height:497px;background:linear-gradient(180deg,#b9cde0 0%,#dfe4e6 35%,#6f8f4e 50%,#c9ab7c 75%,#a98c62 100%)"></div>
<div class="ph" role="img" aria-label="After photo: roof terrace beside red tiled roof and dormer window" style="left:624px;top:2445px;width:355px;height:497px;background:linear-gradient(180deg,#d9dde0 0%,#b3584a 35%,#9b5546 60%,#5e5246 100%)"></div>
<div class="gallery-arrow" style="left:165px;top:2672px;background:var(--blue)">
  <svg width="16" height="12" viewBox="0 0 16 12"><path d="M15 6H2M6 1L1 6l5 5" fill="none" stroke="var(--white)" stroke-width="1.5"/></svg>
</div>
<div class="gallery-arrow" style="left:995px;top:2672px;background:var(--lime)">
  <svg width="16" height="12" viewBox="0 0 16 12"><path d="M1 6h13M10 1l5 5-5 5" fill="none" stroke="var(--white)" stroke-width="1.5"/></svg>
</div>

<!-- call to action & footer -->
<h2 class="cta-title">Ready to <em>transform your</em> property?</h2>
<p class="cta-sub">Contact us today for a free, no-obligation quote.</p>
<a class="btn btn-lime" href="#" style="left:984px;top:3193px;width:126px;height:40px">Contact Us</a>
<div class="rule" style="top:3284px"></div>

<div class="brand" style="left:82px;top:3372px">
  <span class="mark" style="width:40px;height:40px"></span>
  <span style="font-size:30px;color:var(--white)">Hartwell Developments</span>
</div>

<div class="contact-item" style="left:622px">
  <svg width="22" height="22" viewBox="0 0 24 24"><path d="M6.6 10.8a15 15 0 0 0 6.6 6.6l2.2-2.2a1 1 0 0 1 1-.25 11.4 11.4 0 0 0 3.6.57 1 1 0 0 1 1 1V20a1 1 0 0 1-1 1A17 17 0 0 1 3 4a1 1 0 0 1 1-1h3.5a1 1 0 0 1 1 1c0 1.25.2 2.45.57 3.6a1 1 0 0 1-.25 1z" fill="var(--lime)"/></svg>
  <div><p class="label">Call Us</p><p class="value">07700 900418</p></div>
</div>
<div class="contact-item" style="left:863px">
  <svg width="22" height="17" viewBox="0 0 24 18"><rect width="24" height="18" rx="2" fill="var(--lime)"/><path d="M1 2l11 8 11-8" stroke="var(--blue)" stroke-width="2" fill="none"/></svg>
  <div><p class="label">Email Address</p><p class="value">hello@hartwellbuild.co.uk</p></div>
</div>

<div class="rule" style="top:3514px;left:0;width:1200px"></div>
<p class="copyright">© Copyright 2025 Hartwell Developments All Right Reserved</p>
<div class="to-top">
  <svg width="12" height="14" viewBox="0 0 12 14"><path d="M6 13V2M1 6l5-5 5 5" fill="none" stroke="var(--blue)" stroke-width="1.5"/></svg>
</div>

</body>
</html>
```